KLT Proposal Flyer Document

Hi Marketing Team, Require this MS Word doc in a professional proposal flyer format that I can use for proposal to customers, it needs to reflect the KLT Business and Culture, which is a HR Consultancy firm so lots pics of people welcoming, reading at meetings ect, so its people and business focused. Pls note the document needs to be able to be interacted with as well as saved and emailed to clients in PDF format, so pls keep this in mind when doing the design. Thanks very much

Target Market(s)

HR Managers, Global Business Leaders and Decision Makers

Colors
ec1f27

Requirements
Must have
• Professional look

```html
<!DOCTYPE html>
<html lang="en">
<head>
<meta charset="utf-8">
<title>KLT Proposal Flyer</title>
<link rel="stylesheet" href="https://fonts.googleapis.com/css2?family=Montserrat:wght@400;500;600;700;800&display=swap">
<style>
:root{
  --red:#ec1f27;
  --dark:#2b2b2c;
  --black:#161616;
  --paper:#f4f4f4;
  --ink:#1d1d1d;
  --stage:#d9d9d9;
  --placeholder-a:#f1efec;
  --placeholder-b:#e2e0dc;
}
*{box-sizing:border-box;margin:0;padding:0}
html,body{width:1200px;height:2769px;overflow:hidden}
body{background:var(--stage);font-family:'Montserrat',sans-serif;color:var(--ink);position:relative}
.page{position:absolute;width:522px;height:738px;background:linear-gradient(180deg,#fafafa,#eeeeee);overflow:hidden;box-shadow:0 4px 14px rgba(0,0,0,.18)}
.page-large{left:327px;top:177px;transform:scale(1.081);transform-origin:0 0}
.p1{left:61px;top:1193px}
.p2{left:610px;top:1193px}
.p3{left:61px;top:1960px}
.p4{left:612px;top:1960px}

/* brand */
.brand{position:absolute;display:flex;flex-direction:column}
.brand-mark{display:flex;align-items:center;gap:8px}
.brand-dot{width:34px;height:34px;border-radius:50%;background:var(--red)}
.brand-name{font-weight:800;font-size:50px;line-height:1;color:var(--red);letter-spacing:1px}
.brand-sub{font-weight:700;font-size:12.5px;color:var(--red);margin-top:4px;letter-spacing:.2px}
.brand-center{left:0;right:0;top:20px;align-items:center}

/* cover */
.cover-head{position:absolute;left:0;top:0;width:522px;height:226px;background:#fff}
.cover-photo{position:absolute;left:205px;top:0;width:317px;height:226px;background:linear-gradient(120deg,#f3f1ee 0%,#d8d2cb 45%,#8b8580 75%,#c9c3bc 100%)}
.cover-titles{position:absolute;left:23px;top:100px;font-weight:700;font-size:20px;line-height:24px;color:var(--black)}
.pillars{position:absolute;left:0;top:226px;width:522px;height:207px;background:var(--dark)}
.pillars-line{position:absolute;left:103px;right:103px;top:64px;height:3px;background:#fff}
.pillar{position:absolute;top:24px;width:150px;text-align:center;margin-left:-75px}
.pillar-icon{width:76px;height:76px;margin:0 auto;border-radius:50%;background:var(--red);border:3px solid #fff;box-shadow:0 0 0 3px var(--red);display:flex;align-items:center;justify-content:center}
.pillar-label{font-weight:700;font-size:10px;color:var(--red);margin-top:14px}
.pillar-text{font-size:7.6px;line-height:9.4px;color:#e8e8e8;margin-top:6px}
.offer{position:absolute;left:24px;top:446px;width:480px}
.section-title{font-weight:800;font-size:15px;color:var(--red)}
.ticks{list-style:none;margin-top:6px}
.ticks li{position:relative;padding-left:14px;font-size:8.6px;line-height:11px;margin-bottom:8px;font-weight:500}
.ticks li::before{content:"";position:absolute;left:0;top:1px;width:7px;height:7px;border:1.3px solid var(--red);border-radius:50%}
.ticks li::after{content:"";position:absolute;left:2.4px;top:3px;width:2.5px;height:4px;border:solid var(--red);border-width:0 1.3px 1.3px 0;transform:rotate(45deg)}
.band{position:absolute;left:0;top:596px;width:522px;height:134px;background:var(--red)}
.band-tab{position:absolute;left:102px;top:0;width:318px;height:40px;background:var(--black);border-radius:0 0 10px 10px;color:#fff;font-weight:800;font-size:12.3px;line-height:14px;text-align:center;padding-top:6px}
.version{position:absolute;left:18px;top:58px;width:486px;border-collapse:collapse;font-size:9px}
.version th{background:#fff;color:var(--black);font-weight:700;text-align:left;padding:7px 14px;border:1.5px solid #fff}
.version td{color:#fff;padding:10px 14px;border:1.5px solid #fff;height:36px}
.cover-foot{position:absolute;left:0;bottom:0;width:522px;height:8px;background:var(--black)}
.page-no{position:absolute;width:18px;height:18px;border-radius:50%;background:#fff;border:1.5px solid var(--black);font-size:8px;font-weight:800;display:flex;align-items:center;justify-content:center;color:var(--black)}

/* inner pages */
.tagbar{position:absolute;left:0;top:106px;width:522px;height:25px;background:var(--red);color:#fff;font-size:12px;text-align:center;line-height:25px;font-weight:500}
.scope{position:absolute;left:0;top:131px;width:522px;height:111px;background:var(--dark);padding:18px 24px 0}
.scope p{font-size:8.4px;line-height:10.6px;color:#f0f0f0;margin-top:6px}
.lead{position:absolute;left:24px;top:262px;width:478px;font-weight:800;font-size:11.3px;line-height:14px;color:var(--red)}
.scope-list{position:absolute;left:24px;top:322px;width:478px}
.scope-list li{margin-bottom:12px}
.lifecycle-figure{position:absolute;left:25px;top:484px;width:322px;height:194px;background:linear-gradient(135deg,var(--placeholder-a),var(--placeholder-b));border:1px solid #ddd}
.ref-box{position:absolute;left:354px;top:484px;width:143px;height:194px;background:var(--red);color:#fff;font-weight:700;font-size:11.2px;line-height:13.6px;text-align:center;display:flex;align-items:center;justify-content:center;padding:10px}
.footer{position:absolute;left:0;bottom:0;width:522px;height:38px}
.footer-phone{position:absolute;left:0;top:0;width:170px;height:38px;background:var(--black);color:#fff;font-weight:600;font-size:14px;display:flex;align-items:center;gap:7px;padding-left:14px}
.footer-contact{position:absolute;left:170px;top:4px;width:352px;height:28px;background:var(--red);color:#fff;font-size:9.4px;display:flex;align-items:center;gap:8px;padding-left:14px}
.footer .page-no{right:14px;top:9px;left:auto}

/* tables */
.grid{position:absolute;left:17px;width:486px;border-collapse:collapse;font-size:8.6px}
.grid th{background:#fff;font-weight:800;color:var(--black);padding:5px 8px;border:1.5px solid var(--black);text-align:center}
.grid td{border:1.5px solid var(--black);height:23px;padding:3px 8px;font-weight:800;font-size:8.4px}
.grid-dark{border:2px solid var(--black);background:#fff}
.grid-dark td{background:var(--dark);border-color:#fff}
.grid-frame{outline:3px solid var(--black)}
.sub-title{position:absolute;left:23px;font-weight:800;font-size:14.5px;color:var(--red)}
.dark-panel{position:absolute;left:0;top:131px;width:522px;background:var(--dark)}

/* page 4 */
.p4-head{position:absolute;left:24px;width:478px;font-weight:800;font-size:11.6px;line-height:13.5px;color:var(--red)}
.mini{list-style:none;position:absolute;left:24px;width:478px}
.mini li{position:relative;padding-left:11px;font-size:7.7px;line-height:10px;font-weight:500}
.mini li::before{content:"";position:absolute;left:0;top:2px;width:5.5px;height:5.5px;border:1px solid var(--red);border-radius:50%}
.small-p{position:absolute;left:24px;width:478px;font-size:7.8px;line-height:9.6px;font-weight:500}
.rule{position:absolute;left:24px;width:478px;height:1px;background:#777}
</style>
</head>
<body>

<section class="page page-large" aria-label="Proposal cover page">
  <div class="cover-head"></div>
  <div class="cover-photo" role="img" aria-label="Photo of colleagues meeting around a table with a laptop"></div>
  <div class="brand" style="left:23px;top:20px">
    <div class="brand-mark"><span class="brand-dot"></span><span class="brand-name">KLT</span></div>
    <div class="brand-sub">KELTRA BUSINESS CONSULTING</div>
  </div>
  <h1 class="cover-titles">HR Strategy<br>HR Operations<br>HR Projects<br>Business Solutions.</h1>
  <div class="pillars">
    <div class="pillars-line"></div>
    <div class="pillar" style="left:103px">
      <div class="pillar-icon"><svg width="34" height="34" viewBox="0 0 34 34" fill="none" stroke="#fff" stroke-width="2.2"><path d="M3 17c4-7 9-10 14-10s10 3 14 10c-4 7-9 10-14 10S7 24 3 17z"/><circle cx="17" cy="17" r="5"/></svg></div>
      <div class="pillar-label">OUR VISION</div>
      <p class="pillar-text">Build high performing<br>HR Capital Talent and Solutions<br>for local and global business<br>leaders for current and future<br>business needs.</p>
    </div>
    <div class="pillar" style="left:262px">
      <div class="pillar-icon"><svg width="34" height="34" viewBox="0 0 34 34" fill="none" stroke="#fff" stroke-width="2.2"><circle cx="16" cy="18" r="12"/><circle cx="16" cy="18" r="7"/><circle cx="16" cy="18" r="2"/><path d="M16 18L29 5M24 5h5v5"/></svg></div>
      <div class="pillar-label">OUR PURPOSE</div>
      <p class="pillar-text">Our Purpose is to provide<br>HR Strategy, Hands on HR<br>Operational Services and<br>deliver timely Projects to<br>develop, nurture talent and<br>find the best solutions for<br>global business leaders.</p>
    </div>
    <div class="pillar" style="left:419px">
      <div class="pillar-icon"><svg width="34" height="34" viewBox="0 0 34 34" fill="none" stroke="#fff" stroke-width="2.2"><rect x="4" y="5" width="26" height="19"/><path d="M17 24v6M11 30h12M9 19l6-6 4 4 6-6"/></svg></div>
      <div class="pillar-label">OUR STRATEGY</div>
      <p class="pillar-text">To differentiate ourselves<br>based on having a positive<br>impact and providing an<br>exceptional client care<br>experience.</p>
    </div>
  </div>
  <div class="offer">
    <h2 class="section-title">SERVICE OFFERINGS</h2>
    <ul class="ticks">
      <li>Consult with Senior Leaders on critical business issues and find the best solutions.</li>
      <li>Work with the business to Build Strategies across, Employee Branding # Employee Engagement # Performance Management # Talent Management # Best Practices to accelerate business growth.</li>
      <li>Recommend solutions and tools to add structure to the Human Resources function to create employee engagement, positive communications and enable businesses to scale.</li>
      <li>Support business leaders in HR Projects aligned to business improvement and growth.</li>
    </ul>
  </div>
  <div class="band">
    <div class="band-tab">HUMAN RESOURCES STRATEGY,<br>HR OPERATIONS AND HR PROJECTS</div>
    <table class="version">
      <tr><th style="width:20%">VERSION</th><th style="width:30%">ISSUE DATE</th><th>PROJECT</th></tr>
      <tr><td>1.0</td><td>2020</td><td>Consultation with Business.<br>Sample Project Framework.</td></tr>
    </table>
  </div>
  <div class="cover-foot"></div>
  <div class="page-no" style="left:487px;top:714px">1</div>
</section>

<section class="page p1" aria-label="Proposal page 1">
  <div class="cover-head"></div>
  <div class="cover-photo" role="img" aria-label="Photo of colleagues meeting around a table with a laptop"></div>
  <div class="brand" style="left:23px;top:20px">
    <div class="brand-mark"><span class="brand-dot"></span><span class="brand-name">KLT</span></div>
    <div class="brand-sub">KELTRA BUSINESS CONSULTING</div>
  </div>
  <h1 class="cover-titles">HR Strategy<br>HR Operations<br>HR Projects<br>Business Solutions.</h1>
  <div class="pillars">
    <div class="pillars-line"></div>
    <div class="pillar" style="left:103px">
      <div class="pillar-icon"><svg width="34" height="34" viewBox="0 0 34 34" fill="none" stroke="#fff" stroke-width="2.2"><path d="M3 17c4-7 9-10 14-10s10 3 14 10c-4 7-9 10-14 10S7 24 3 17z"/><circle cx="17" cy="17" r="5"/></svg></div>
      <div class="pillar-label">OUR VISION</div>
      <p class="pillar-text">Build high performing<br>HR Capital Talent and Solutions<br>for local and global business<br>leaders for current and future<br>business needs.</p>
    </div>
    <div class="pillar" style="left:262px">
      <div class="pillar-icon"><svg width="34" height="34" viewBox="0 0 34 34" fill="none" stroke="#fff" stroke-width="2.2"><circle cx="16" cy="18" r="12"/><circle cx="16" cy="18" r="7"/><circle cx="16" cy="18" r="2"/><path d="M16 18L29 5M24 5h5v5"/></svg></div>
      <div class="pillar-label">OUR PURPOSE</div>
      <p class="pillar-text">Our Purpose is to provide<br>HR Strategy, Hands on HR<br>Operational Services and<br>deliver timely Projects to<br>develop, nurture talent and<br>find the best solutions for<br>global business leaders.</p>
    </div>
    <div class="pillar" style="left:419px">
      <div class="pillar-icon"><svg width="34" height="34" viewBox="0 0 34 34" fill="none" stroke="#fff" stroke-width="2.2"><rect x="4" y="5" width="26" height="19"/><path d="M17 24v6M11 30h12M9 19l6-6 4 4 6-6"/></svg></div>
      <div class="pillar-label">OUR STRATEGY</div>
      <p class="pillar-text">To differentiate ourselves<br>based on having a positive<br>impact and providing an<br>exceptional client care<br>experience.</p>
    </div>
  </div>
  <div class="offer">
    <h2 class="section-title">SERVICE OFFERINGS</h2>
    <ul class="ticks">
      <li>Consult with Senior Leaders on critical business issues and find the best solutions.</li>
      <li>Work with the business to Build Strategies across, Employee Branding # Employee Engagement # Performance Management # Talent Management # Best Practices to accelerate business growth.</li>
      <li>Recommend solutions and tools to add structure to the Human Resources function to create employee engagement, positive communications and enable businesses to scale.</li>
      <li>Support business leaders in HR Projects aligned to business improvement and growth.</li>
    </ul>
  </div>
  <div class="band">
    <div class="band-tab">HUMAN RESOURCES STRATEGY,<br>HR OPERATIONS AND HR PROJECTS</div>
    <table class="version">
      <tr><th style="width:20%">VERSION</th><th style="width:30%">ISSUE DATE</th><th>PROJECT</th></tr>
      <tr><td>1.0</td><td>2020</td><td>Consultation with Business.<br>Sample Project Framework.</td></tr>
    </table>
  </div>
  <div class="cover-foot"></div>
  <div class="page-no" style="left:487px;top:714px">1</div>
</section>

<section class="page p2" aria-label="Proposal page 2">
  <div class="brand brand-center">
    <div class="brand-mark"><span class="brand-dot"></span><span class="brand-name">KLT</span></div>
    <div class="brand-sub">KELTRA BUSINESS CONSULTING</div>
  </div>
  <div class="tagbar">HR Strategy | HR Operations | HR Projects | Business Solutions.</div>
  <div class="scope">
    <h2 class="section-title">1. PROJECT SCOPE</h2>
    <p>Initial communication to understand current HR Framework in place or leverage from Regional/Global Head Office. Understanding the current HR Model in place and Assessment of current HR Practices across the HR Employee Lifecycle and key business strategies and goals currently in place.</p>
  </div>
  <p class="lead">The main areas of focus is an initial conversation regards to understanding of the current HR Landscape, current Model in Place, current practices, systems and policies across the organization.</p>
  <ul class="ticks scope-list">
    <li>Review and understand current HR Practices, culture, values and work environment. Style of business structure and leadership in place currently.</li>
    <li>Current HR Model in place, current systems, practices across the Employee Lifecycle as aligned to Principles of Fair Employment Practices, FEPA Guidelines and The Connected Workplace Model as a reference model.</li>
    <li>Key Business Goals, Strategy, Plans and Priorities current and the future.</li>
    <li>Gain an understanding of current Employee Pulse and any Recent Surveys</li>
    <li>Gain an understanding of current Safety Strategy that is in place with Covid-19, review policies to date.</li>
  </ul>
  <div class="lifecycle-figure" role="img" aria-label="Employee lifecycle model diagram from the connected workplace reference"></div>
  <div class="ref-box">“Hire, Inspire, Retire” Approach Reference: Adopted from the Connected Workplace Employee Lifecycle Model, Author: Marion Hale</div>
  <div class="footer">
    <div class="footer-phone"><svg width="16" height="16" viewBox="0 0 16 16" fill="none" stroke="#fff" stroke-width="1.4"><circle cx="8" cy="8" r="7"/><path d="M5.5 4.5l1.5 2-1 1c.6 1.2 1.3 1.9 2.5 2.5l1-1 2 1.5-1 1.5c-3 0-6-3-6-6z"/></svg>(123) 4567-7890</div>
    <div class="footer-contact"><span>&#9993; info@emailaddress.com</span><span>&#9737; www.websiteaddress.com</span></div>
    <div class="page-no">2</div>
  </div>
</section>

<section class="page p3" aria-label="Proposal page 3">
  <div class="brand brand-center">
    <div class="brand-mark"><span class="brand-dot"></span><span class="brand-name">KLT</span></div>
    <div class="brand-sub">KELTRA BUSINESS CONSULTING</div>
  </div>
  <div class="tagbar">HR Strategy | HR Operations | HR Projects | Business Solutions.</div>
  <div class="dark-panel" style="height:8px"></div>
  <h2 class="sub-title" style="top:140px">2. PROJECT RESOURCES</h2>
  <table class="grid grid-dark" style="top:168px">
    <tr><th style="width:25%">RESOURCES</th><th style="width:36%">VALUE ADD POSITION</th><th>YEARS OF EXPERIENCE</th></tr>
    <tr><td></td><td></td><td></td></tr><tr><td></td><td></td><td></td></tr>
    <tr><td></td><td></td><td></td></tr><tr><td></td><td></td><td></td></tr>
    <tr><td></td><td></td><td></td></tr>
  </table>
  <h2 class="sub-title" style="top:336px">3. PROJECT BUDGET</h2>
  <table class="grid grid-frame" style="top:362px">
    <tr><th style="width:50%;text-align:left;padding-left:26px">PROJECT BUDGET</th><th colspan="2">FORECAST COST</th><th colspan="2">REAL COST</th></tr>
    <tr><td></td><td>$</td><td style="text-align:center">TIME</td><td>$</td><td style="text-align:center">TIME</td></tr>
    <tr><td></td><td></td><td></td><td></td><td></td></tr><tr><td></td><td></td><td></td><td></td><td></td></tr>
    <tr><td></td><td></td><td></td><td></td><td></td></tr><tr><td></td><td></td><td></td><td></td><td></td></tr>
    <tr><td></td><td></td><td></td><td></td><td></td></tr>
  </table>
  <h2 class="sub-title" style="top:552px">4. PROJECT MILESTONES MAJOR TASKS</h2>
  <table class="grid grid-frame" style="top:578px;font-size:7.6px">
    <tr><th>TASK NAME</th><th>ASSIGNED TO</th><th>START DATE</th><th>END DATE</th><th>DURATION in days</th><th>STATUS</th></tr>
    <tr><td style="height:46px">PROJECT<br>ASSESSMENT.</td><td>DANA<br>REYES</td><td></td><td></td><td></td><td></td></tr>
  </table>
  <div class="footer">
    <div class="footer-phone"><svg width="16" height="16" viewBox="0 0 16 16" fill="none" stroke="#fff" stroke-width="1.4"><circle cx="8" cy="8" r="7"/><path d="M5.5 4.5l1.5 2-1 1c.6 1.2 1.3 1.9 2.5 2.5l1-1 2 1.5-1 1.5c-3 0-6-3-6-6z"/></svg>(123) 4567-7890</div>
    <div class="footer-contact"><span>&#9993; info@emailaddress.com</span><span>&#9737; www.websiteaddress.com</span></div>
    <div class="page-no">3</div>
  </div>
</section>

<section class="page p4" aria-label="Proposal page 4">
  <div class="brand brand-center">
    <div class="brand-mark"><span class="brand-dot"></span><span class="brand-name">KLT</span></div>
    <div class="brand-sub">KELTRA BUSINESS CONSULTING</div>
  </div>
  <div class="tagbar">HR Strategy | HR Operations | HR Projects | Business Solutions.</div>
  <h2 class="p4-head" style="top:146px">Initial Conversation, Collaboration with HR Leadership Team and Senior Management.</h2>
  <ul class="mini" style="top:184px">
    <li>Assessment of current HR Employee Lifecycle and current business goals in place</li>
    <li>HR Health Check in terms of current strategies in place, practices, processes and systems in place.</li>
    <li>How does the website look for attracting new employees ?</li>
    <li>Are there clear job specifications in place ?</li>
    <li>How developed is the Employee Handbook ?</li>
    <li>Current framework and policies in place ?</li>
    <li>Is there an employee referral program in place ?</li>
    <li>What is the level of sophistication across the HR Strategy ?</li>
    <li>What are the business key goals ?</li>
    <li>What are the business key priorities ?</li>
    <li>Which technology is in place for recruiting ?</li>
    <li>Is there Regular and Ongoing Performance Management ?</li>
    <li>Which technology is in place for learning and development ?</li>
    <li>What sort of engagement strategies are currently in place for employees ?</li>
    <li>Have any recent ' Employee Pulse surveys been conducted ?</li>
    <li>What was the result of the last ' Employee Survey ' in terms of NPS – Net Promoter Score, How satisfied where employees with working at the company ?</li>
    <li>What would management and the leadership team like help with ?</li>
  </ul>
  <h2 class="p4-head" style="top:398px">Human Resources, Leadership Team, Senior Management Perspective ?</h2>
  <ul class="mini" style="top:416px"><li>Feedback and open dialogue to the above questions.</li></ul>
  <h2 class="p4-head" style="top:446px">5. Communication Plan</h2>
  <p class="small-p" style="top:462px">Per weekly Team meetings each Friday on VideoMeet with Team Members for full Team Engagement to keep communications positive and open for WFH, remote workers and those back in the office.</p>
  <div class="rule" style="top:494px"></div>
  <h2 class="p4-head" style="top:509px">6. Other Team Member Ideas.</h2>
  <div class="rule" style="top:536px"></div>
  <h2 class="p4-head" style="top:552px">7. Emphasis on Quality and Best Practices.</h2>
  <div class="rule" style="top:577px"></div>
  <h2 class="p4-head" style="top:592px">8. HR Analytics and Insights.</h2>
  <p class="small-p" style="top:608px">Sample HR Metrics that are data driven and can be insightful for Business Performance and track performance, to gain insight and from this data build out Career Development Maps to help team members grow, build individual capabilities and competencies to drive engagement and accelerate business performance.</p>
  <p class="small-p" style="top:654px">For Example: Employee Performance Metrics.</p>
  <div class="footer">
    <div class="footer-phone"><svg width="16" height="16" viewBox="0 0 16 16" fill="none" stroke="#fff" stroke-width="1.4"><circle cx="8" cy="8" r="7"/><path d="M5.5 4.5l1.5 2-1 1c.6 1.2 1.3 1.9 2.5 2.5l1-1 2 1.5-1 1.5c-3 0-6-3-6-6z"/></svg>(123) 4567-7890</div>
    <div class="footer-contact"><span>&#9993; info@emailaddress.com</span><span>&#9737; www.websiteaddress.com</span></div>
    <div class="page-no">4</div>
  </div>
</section>

</body>
</html>
```